Postcard Design

Bramble Circuit Holdings is a waste and Recycling company. We want to purchase recyclable materials from businesses. We would like to use the colors green and grey. The exact colors needed in this project are described below. We would like to have a picture of waste cardboard,a picture of money, and and the line- Are you getting top dollar for your Recyclables? After please put our logo and our phone number: 800.472.5196, our website (tindlepath.com),
and our email address: marguerite@tindlepath.com.

* Postcard must contain our logo. Please see buisness card for branding

Industry/Entity Type

It Company

Requirements
Must have
• This postcard must contain the logo and these colors:
Pantone: 576C & 418C

```html
<!DOCTYPE html>
<html lang="en">
<head>
<meta charset="utf-8">
<title>Bramble Circuit Holdings – Postcard</title>
<link rel="stylesheet" href="https://fonts.googleapis.com/css2?family=Montserrat:wght@400;500;700&family=Arimo:wght@400;700&display=swap">
<style>
  :root {
    --green: #5cb612;
    --green-soft: #e6f1dc;
    --charcoal: #2f3030;
    --slate: #4b524e;
    --page: #edf2f2;
    --card-grey-top: #dcdbde;
    --card-grey-mid: #f3f3f4;
    --card-grey-bottom: #c9c9cc;
    --rule: #6d6d6d;
    --white: #ffffff;
  }
  * { margin: 0; padding: 0; box-sizing: border-box; }
  html, body { width: 1200px; height: 1000px; overflow: hidden; }
  body { background: var(--page); position: relative; font-family: "Montserrat", sans-serif; }

  /* Front side */
  .postcard-front {
    position: absolute; left: 98px; top: 187px; width: 464px; height: 600px;
    background: linear-gradient(180deg, var(--card-grey-top) 0%, var(--card-grey-mid) 48%, var(--white) 62%, var(--card-grey-mid) 82%, var(--card-grey-bottom) 100%);
    overflow: hidden;
  }
  .headline { position: absolute; left: 62px; top: 50px; color: var(--charcoal); text-transform: uppercase; }
  .headline-lead { font-size: 35px; font-weight: 400; letter-spacing: 3.2px; line-height: 1; }
  .headline-main { font-size: 51px; font-weight: 700; letter-spacing: 1px; line-height: 1; margin-top: 12px; }
  .headline-tail { font-size: 24px; font-weight: 400; letter-spacing: 2.4px; line-height: 1; margin-top: 12px; }
  .accent { color: var(--green); }
  .question-mark {
    position: absolute; left: 190px; top: 168px; width: 100px; text-align: center;
    font-size: 160px; font-weight: 700; color: var(--green); line-height: 1;
  }
  .photo { position: absolute; }
  .photo-cardboard { left: 32px; top: 312px; width: 166px; height: 98px; }
  .photo-coins { left: 280px; top: 308px; width: 136px; height: 102px; }
  .equals { position: absolute; left: 229px; top: 365px; width: 17px; }
  .equals span { display: block; height: 4px; background: var(--charcoal); margin-bottom: 4px; }

  .contact-panel {
    position: absolute; left: 52px; top: 447px; width: 412px; height: 121px; background: var(--white);
  }
  .contact-frame {
    position: absolute; left: 10px; top: 9px; right: 0; bottom: 7px;
    border: 1px dashed var(--rule); border-right: none;
  }
  .contact-list { position: absolute; left: 10px; top: 9px; width: 215px; height: 105px; border-right: 1px dashed var(--rule); }
  .contact-row { height: 26.25px; border-bottom: 1px dashed var(--rule); text-align: right; padding-right: 16px; }
  .contact-row:last-child { border-bottom: none; }
  .contact-label { color: var(--green); font-size: 14px; letter-spacing: 1px; line-height: 26px; }
  .contact-value { color: var(--slate); font-size: 15px; font-weight: 500; letter-spacing: 1.4px; line-height: 27px; }
  .brand-lockup {
    position: absolute; left: 236px; top: 20px; width: 168px; height: 82px;
    display: flex; flex-direction: column; align-items: center; justify-content: center; gap: 8px;
  }
  .brand-mark { width: 22px; height: 22px; background: var(--green); }
  .brand-name { font-size: 14px; font-weight: 700; color: var(--slate); text-align: center; line-height: 1.2; }

  /* Back side */
  .postcard-back {
    position: absolute; left: 609px; top: 325px; width: 503px; height: 389px; background: var(--white);
  }
  .side-band { position: absolute; left: 0; top: 0; width: 23px; height: 100%; background: var(--green); }
  .stamp-box { position: absolute; left: 378px; top: 20px; width: 107px; height: 105px; border: 1px solid var(--rule); }
  .address-lines { position: absolute; left: 271px; top: 170px; width: 208px; }
  .address-lines span { display: block; height: 1px; background: var(--rule); margin-bottom: 28px; }
  .address-lines span:not(:first-child) { margin-left: 4px; }
  .sender { position: absolute; left: 50px; top: 185px; width: 162px; text-align: center; font-family: "Arimo", sans-serif; }
  .sender .brand-lockup { position: static; width: auto; height: 64px; gap: 6px; }
  .sender-details { font-size: 11px; line-height: 13.3px; color: var(--charcoal); font-style: normal; margin-top: 2px; }
  .sender-web { font-size: 13px; font-weight: 700; color: var(--green); margin-top: 2px; }
</style>
</head>
<body>

<section class="postcard-front" aria-label="Postcard front">
  <h1 class="headline">
    <span class="headline-lead" style="display:block">Are you getting</span>
    <span class="headline-main" style="display:block">Top <span class="accent">Dollar</span></span>
    <span class="headline-tail" style="display:block">For your <span class="accent">Recyclabes</span></span>
  </h1>
  <div class="question-mark" aria-hidden="true">?</div>

  <svg class="photo photo-cardboard" role="img" aria-label="Photo of a pile of waste cardboard boxes" viewBox="0 0 166 98" preserveAspectRatio="none">
    <defs>
      <radialGradient id="cardboard-tone" cx="50%" cy="50%" r="55%">
        <stop offset="0" stop-color="#c99a63"/>
        <stop offset="0.7" stop-color="#b88650"/>
        <stop offset="1" stop-color="#b88650" stop-opacity="0"/>
      </radialGradient>
    </defs>
    <rect width="166" height="98" fill="url(#cardboard-tone)"/>
  </svg>

  <div class="equals" aria-hidden="true"><span></span><span></span></div>

  <svg class="photo photo-coins" role="img" aria-label="Photo of a stack of copper coins" viewBox="0 0 136 102" preserveAspectRatio="none">
    <defs>
      <radialGradient id="coin-tone" cx="50%" cy="50%" r="55%">
        <stop offset="0" stop-color="#9a4a28"/>
        <stop offset="0.7" stop-color="#7a351c"/>
        <stop offset="1" stop-color="#7a351c" stop-opacity="0"/>
      </radialGradient>
    </defs>
    <rect width="136" height="102" fill="url(#coin-tone)"/>
  </svg>

  <div class="contact-panel">
    <div class="contact-frame"></div>
    <div class="contact-list">
      <div class="contact-row"><span class="contact-label">our website</span></div>
      <div class="contact-row"><span class="contact-value">www.tindlepath.com</span></div>
      <div class="contact-row"><span class="contact-label">our phone</span></div>
      <div class="contact-row"><span class="contact-value">800.472.5196</span></div>
    </div>
    <div class="brand-lockup">
      <span class="brand-mark" aria-hidden="true"></span>
      <span class="brand-name">Bramble Circuit Holdings</span>
    </div>
  </div>
</section>

<section class="postcard-back" aria-label="Postcard back">
  <div class="side-band"></div>
  <div class="stamp-box" aria-label="Stamp area"></div>
  <div class="address-lines" aria-hidden="true"><span></span><span></span><span></span><span></span></div>

  <div class="sender">
    <div class="brand-lockup">
      <span class="brand-mark" aria-hidden="true"></span>
      <span class="brand-name">Bramble Circuit Holdings</span>
    </div>
    <address class="sender-details">
      418 Larkspur Avenue<br>
      Fenwick, CA 90412<br>
      Phone: (800) 472-5196<br>
      Email: marguerite@tindlepath.com
    </address>
    <div class="sender-web">www.tindlepath.com</div>
  </div>
</section>

</body>
</html>
```